Business Cards for a law firm

Business cards for our law firm. Use our silhoette logo and OAK HARBOR - check our website (www.oakharbor-legal.com)

Contact Information for Business Card

our silhouette logo, OAK HARBOR, 800-555-0147, Dorian Kestrup, dorian@oakharbor-legal.com

Requirements
Must have
• our silhouette logo, OAK HARBOR, 800-555-0147, Dorian Kestrup, dorian@oakharbor-legal.com

```html
<!DOCTYPE html>
<html lang="en">
<head>
<meta charset="utf-8">
<title>Oak Harbor – Business Cards</title>
<link rel="stylesheet" href="https://fonts.googleapis.com/css2?family=Montserrat:wght@600&family=Open+Sans:wght@400;700&display=swap">
<style>
  :root {
    --navy: #1b2f6b;
    --amber: #f9a81f;
    --white: #ffffff;
    --backdrop: #e6e6e6;
  }
  * { box-sizing: border-box; margin: 0; padding: 0; }
  html, body { width: 1200px; height: 977px; overflow: hidden; }
  body {
    background: var(--backdrop);
    position: relative;
    font-family: "Open Sans", sans-serif;
    color: var(--navy);
  }
  .card {
    position: absolute;
    left: 220px;
    width: 760px;
    height: 434px;
    border-radius: 26px;
    overflow: hidden;
    box-shadow: 0 6px 18px rgba(0,0,0,0.18);
  }
  .card--front { top: 40px; background: var(--white); }
  .card--back { top: 503px; background: var(--amber); }

  .front-brand {
    position: absolute;
    left: 150px;
    top: 180px;
    display: flex;
    align-items: center;
    gap: 22px;
  }
  .front-brand__mark {
    width: 44px; height: 44px;
    background: var(--navy);
  }
  .front-brand__name {
    font-family: "Montserrat", sans-serif;
    font-weight: 600;
    font-size: 52px;
    letter-spacing: 5px;
    color: var(--navy);
  }

  .back-brand {
    position: absolute;
    right: 52px;
    top: 44px;
    font-family: "Open Sans", sans-serif;
    font-weight: 700;
    font-size: 22px;
    letter-spacing: 2px;
    color: var(--navy);
  }

  .identity {
    position: absolute;
    right: 420px;
    top: 238px;
    text-align: right;
  }
  .identity__name {
    font-weight: 700;
    font-size: 38px;
    line-height: 1.1;
    white-space: nowrap;
  }
  .identity__title {
    font-size: 22px;
    margin-top: 2px;
  }

  .divider {
    position: absolute;
    left: 362px;
    top: 222px;
    width: 2px;
    height: 96px;
    background: var(--navy);
  }

  .contact {
    position: absolute;
    left: 384px;
    top: 224px;
    list-style: none;
  }
  .contact__item {
    display: flex;
    align-items: center;
    gap: 12px;
    font-size: 18px;
    line-height: 30px;
    white-space: nowrap;
  }
  .contact__item--phone { font-weight: 700; font-size: 20px; }
  .contact__icon { width: 16px; height: 16px; flex: none; }
</style>
</head>
<body>

<section class="card card--front" aria-label="Business card front">
  <div class="front-brand">
    <span class="front-brand__mark"></span>
    <span class="front-brand__name">OAK HARBOR</span>
  </div>
</section>

<section class="card card--back" aria-label="Business card back">
  <div class="back-brand">OAK HARBOR</div>

  <div class="identity">
    <p class="identity__name">DORIAN KESTRUP</p>
    <p class="identity__title">Attorney</p>
  </div>

  <div class="divider"></div>

  <ul class="contact">
    <li class="contact__item contact__item--phone">
      <svg class="contact__icon" viewBox="0 0 16 16" aria-hidden="true">
        <path d="M3.5 1.5l2.5 0 1 3.2-1.6 1.2c.9 1.8 2.3 3.2 4.1 4.1l1.2-1.6 3.2 1v2.5c0 .8-.7 1.5-1.5 1.5C6.6 13.4 2.6 9.4 2 3c0-.8.7-1.5 1.5-1.5z" fill="#1b2f6b"/>
      </svg>
      (800) 555-0147
    </li>
    <li class="contact__item">
      <svg class="contact__icon" viewBox="0 0 16 16" aria-hidden="true">
        <rect x="1" y="3" width="14" height="10" fill="#1b2f6b"/>
        <path d="M1.5 3.5L8 9l6.5-5.5" fill="none" stroke="#f9a81f" stroke-width="1.3"/>
      </svg>
      dorian@oakharbor-legal.com
    </li>
    <li class="contact__item">
      <svg class="contact__icon" viewBox="0 0 16 16" aria-hidden="true">
        <circle cx="8" cy="8" r="7" fill="#1b2f6b"/>
        <path d="M1 8h14M8 1c-2.5 2.5-2.5 11.5 0 14M8 1c2.5 2.5 2.5 11.5 0 14" fill="none" stroke="#f9a81f" stroke-width="1"/>
      </svg>
      www.oakharbor-legal.com
    </li>
  </ul>
</section>

</body>
</html>
```